Powerpoint design template for FLOMBIRT for new digital platform

We would like to use a PowerPoint template, we would like to create a new page, we would like to create a new digital platform FLOMBIRT for schools and parents for the creation of playful communication and educational tools for children to enhance their positive development, amaze them learn in a playful way. This platform is going to be the most creative, stimulating and innovative classroom, easy to use and fast to implement. Scrapbooking, collages ... Magazine, newsletters Diplomla / awards Slideshows Facebook Calendars Organizers Greetings Games ... This powerpoint template will be used essential to We are looking for a professional design, positioning our brand in the children market with an adult hearing. so you will need to find a good deal. Primary target: nurseries & schools from 0 to 18 years old and universities (in 2nd phase) Secondary target: small & medium businesses Third target: general public, and TPE If it is a color scheme, then it is suggested that it be marketed in Europe (UK, Italy, Spain) and in a 2nd Stage USA and other countries. multiple options for front page, insidious pages (multiple styles with limited text and extended text) and final contact page We need something to read, we can not do it too much, but we can not do it. , and inside pages aligned to our logo

Target Market(s)

Target 1; Education with teacher Target 2; parents and grandparents

Industry/Entity Type

Education

Font styles to use
Other font styles liked:
• not decided. but not too fancy

Requirements
Must have
• Multi page options for front page, page insides (multiple styles with limited text and extended text) and final page contact
Nice to have
• do not have a lot of ideas. We need something to read, we can not get away from it
Should not have
• not too fancy and busy: keep clarity & simplicity while reassuring on quality

```html
<!DOCTYPE html>
<html lang="en">
<head>
<meta charset="utf-8">
<title>FLOMBIRT – Section Slide</title>
<link href="https://fonts.googleapis.com/css2?family=Roboto+Condensed:wght@400;700&display=swap" rel="stylesheet">
<style>
  :root {
    --cyan: #1bb8e8;
    --magenta: #e8388f;
    --text-dark: #2a2a2a;
    --lime: #d6e03d;
    --lime-light: #e9ef9a;
    --orange: #f7941d;
    --photo-top: #eef4f8;
    --photo-warm: #f3e6d8;
    --photo-cool: #dbe9f2;
    --white: #ffffff;
  }
  * { margin: 0; padding: 0; box-sizing: border-box; }
  html, body { width: 1200px; height: 900px; overflow: hidden; background: var(--white); }
  body { font-family: "Roboto Condensed", "Arial Narrow", sans-serif; }

  .slide { position: relative; width: 1200px; height: 900px; overflow: hidden; }

  .hero-photo {
    position: absolute; left: 0; top: 0; width: 1200px; height: 834px;
    background:
      radial-gradient(ellipse 380px 300px at 620px 380px, var(--photo-warm), transparent 70%),
      radial-gradient(ellipse 340px 300px at 980px 360px, var(--photo-warm), transparent 70%),
      radial-gradient(ellipse 300px 260px at 220px 300px, #f4e2d4, transparent 70%),
      linear-gradient(180deg, var(--photo-top) 0%, var(--photo-cool) 55%, #f2f2e6 100%);
  }

  .brand {
    position: absolute; right: 18px; top: 22px;
    display: flex; align-items: center; gap: 12px;
  }
  .brand-mark { width: 26px; height: 26px; background: var(--lime); }
  .brand-text { display: flex; flex-direction: column; }
  .brand-name { font-weight: 700; font-size: 40px; line-height: 1; color: var(--magenta); letter-spacing: 1px; }
  .brand-tagline { font-size: 11px; line-height: 1.2; color: var(--text-dark); letter-spacing: 1px; margin-top: 6px; text-transform: uppercase; }

  .section-heading {
    position: absolute; left: 0; top: 372px; width: 1190px; text-align: center;
    font-weight: 700; font-size: 66px; line-height: 1; letter-spacing: 1px;
  }
  .section-heading .accent-cyan { color: var(--cyan); }
  .section-heading .accent-magenta { color: var(--magenta); }

  .section-intro {
    position: absolute; left: 110px; top: 468px; width: 960px; text-align: center;
    font-size: 22.5px; line-height: 34px; color: var(--text-dark);
  }

  .footer { position: absolute; left: 0; top: 834px; width: 1200px; height: 66px; }
  .footer svg { position: absolute; left: 0; top: 0; }
  .footer-url {
    position: absolute; left: 21px; top: 18px;
    font-size: 24px; color: var(--text-dark);
  }
  .footer-page {
    position: absolute; right: 36px; top: 19px;
    font-size: 22px; color: var(--text-dark);
  }
</style>
</head>
<body>
  <main class="slide">
    <div class="hero-photo" role="img" aria-label="Soft, faded classroom photo of smiling schoolchildren at desks with coloured pencils"></div>

    <div class="brand">
      <span class="brand-mark"></span>
      <div class="brand-text">
        <span class="brand-name">FLOMBIRT</span>
        <span class="brand-tagline">Your tagline<br>goes here</span>
      </div>
    </div>

    <h1 class="section-heading">
      <span class="accent-cyan">SECTION</span> <span class="accent-magenta">TITLE HERE</span>
    </h1>
    <p class="section-intro">Bear claw croissant apple pie. Croissant cake tart liquorice tart pastry. Tiramisu apple pie biscuit sweet oat cake sweet icing brownie.</p>

    <footer class="footer">
      <svg width="1200" height="66" viewBox="0 0 1200 66">
        <rect x="0" y="0" width="1200" height="66" fill="var(--lime)"/>
        <polygon points="975,0 1010,0 1068,66 1033,66" fill="var(--lime-light)"/>
        <polygon points="996,0 1200,0 1200,66 1054,66" fill="var(--white)"/>
        <polygon points="1006,0 1200,0 1200,66 1064,66" fill="var(--orange)"/>
      </svg>
      <span class="footer-url">www.flombirt.com</span>
      <span class="footer-page">Page : 01</span>
    </footer>
  </main>
</body>
</html>
```